Energy Solution company Needs a PowerPoint Design

We need a PowerPoint design for new energy solution company based in Houston. major markets / clients in Africa called ''RW Fjordvik Solutions'' . We provider variety of professional services, systems ,and project management solutions to Oil & Gas, Power , Telecommunication , ICT, Airlines & Transportation , Social & Public Sector and Utilities & Alternative Energy industries. We would like to see a simple PowerPoint designs but statement. The final design should communicate engineering Integrity, quality and safety. See attached file with template and company logo. please use logo color combination.

Target Market(s)

Oil & Gas, Power , Telecommunication , ICT, Airlines & Transportation , Social & Public Sector and Utilities & Alternative Energy industries.

Industry/Entity Type

It Company

Font styles to use
Other font styles liked:
• Century Gothic

Colors
ffc214
aaaaaa
0355a3

Requirements
Must have
• engineering details oriented simple looks. SEE ATTACHED PPT WITH COMPANY LOGO AND TEMPLATE. PLEASE ATTACHED LOGO COLOR COMBINATION.]
• We will like to see 5 text boxes with different images across the middle of the cover page, this images will be from below Industries:
• • Oil and Gas
• • Power
• • Information Technology
• • Manufacturing Industry
• • Higher Education Industry
• Please don't include the Industries name as list above, We just want the images.
Nice to have
• • Oil and Gas
• • Power

```html
<!DOCTYPE html>
<html lang="en">
<head>
<meta charset="UTF-8">
<title>Gas Plant Upgrade — RW Fjordvik Solutions</title>
<link rel="stylesheet" href="https://fonts.googleapis.com/css2?family=Roboto:wght@400;500&display=swap">
<style>
  :root {
    --brand-navy: #03446d;
    --brand-blue: #0355a3;
    --brand-amber: #ffc214;
    --brand-grey: #aaaaaa;
    --subtitle-blue: #0b4a74;
    --body-ink: #222222;
    --footer-grey: #909090;
    --paper: #ffffff;
    --header-text: #ffffff;
  }
  * { margin: 0; padding: 0; box-sizing: border-box; }
  html, body {
    width: 1200px;
    height: 900px;
    overflow: hidden;
    background: var(--paper);
  }
  .slide {
    position: relative;
    width: 1200px;
    height: 900px;
    background: var(--paper);
    font-family: "Roboto", sans-serif;
    overflow: hidden;
  }
  .slide-header {
    position: absolute;
    left: 0; top: 0;
    width: 1200px;
    height: 112px;
    background: var(--brand-navy);
    display: flex;
    align-items: center;
    justify-content: space-between;
    padding: 0 36px 0 27px;
  }
  .slide-title {
    color: var(--header-text);
    font-size: 57px;
    font-weight: 500;
    letter-spacing: 0.5px;
  }
  .brand-name {
    display: flex;
    align-items: center;
    gap: 10px;
    color: var(--header-text);
    font-size: 20px;
    font-weight: 500;
  }
  .brand-name .brand-square {
    width: 18px;
    height: 18px;
    background: var(--header-text);
  }
  .content-column {
    position: absolute;
    left: 53px;
    top: 188px;
    width: 560px;
  }
  .slide-subtitle {
    color: var(--subtitle-blue);
    font-size: 27px;
    font-weight: 500;
    line-height: 34px;
    margin-bottom: 2px;
  }
  .body-copy {
    color: var(--body-ink);
    font-size: 21px;
    line-height: 36px;
    white-space: pre;
  }
  .body-copy + .body-copy { margin-top: 36px; }
  .image-slot {
    position: absolute;
    left: 673px;
    width: 463px;
    height: 272px;
  }
  .image-slot.top {
    top: 205px;
    background: linear-gradient(180deg, #2f5f86 0%, #7d8fa0 55%, #c9a24a 100%);
  }
  .image-slot.bottom {
    top: 522px;
    background: linear-gradient(180deg, #5d86b3 0%, #8fa6bd 50%, #6f7a84 100%);
  }
  .slide-footer {
    position: absolute;
    left: 0; bottom: 0;
    width: 1200px;
    height: 45px;
    background: var(--footer-grey);
  }
</style>
</head>
<body>
  <main class="slide">
    <header class="slide-header">
      <h1 class="slide-title">Gas Plant Upgrade</h1>
      <div class="brand-name"><span class="brand-square"></span>RW Fjordvik Solutions</div>
    </header>

    <section class="content-column">
      <h2 class="slide-subtitle">Engineering Overview</h2>
      <p class="body-copy">RW Fjordvik Solutions delivered a full upgrade of
the gas compression station, covering design,
procurement, installation and commissioning of
all control systems. Our engineers worked with
the client's operations team to keep the plant
online while new safety interlocks, metering and
remote monitoring were brought into service.
Every stage followed a strict quality plan, with
independent inspections at each hold point and
zero lost-time incidents recorded across the
full project life.</p>
      <p class="body-copy"> The new power supply now serves three substations
and a regional telecom hub, cutting unplanned
downtime and giving the client live plant data.</p>
    </section>

    <div class="image-slot top" role="img" aria-label="Photo of a gas compression plant at dusk"></div>
    <div class="image-slot bottom" role="img" aria-label="Photo of power transmission lines and a substation"></div>

    <footer class="slide-footer"></footer>
  </main>
</body>
</html>
```